Keys to Rise - Tri-Fold Brochure

For more than three decades, www.ferndaleunion.org has been the leading service provider and community advocate for Marin’s low-income, Spanish-speaking immigrants. Our organization addresses the specific needs of Spanish-speaking immigrants by giving them the tools they need to move out of poverty and work toward greater well-being and stability, legal status, economic independence and self-sufficiency so they can integrate into American society as contributing and thriving community members.

"Keys to Rise" = Skills and Abilities

*Bilingual skills (English & Spanish)
*Technology skills
*Work readiness skills
*Financial literacy skills
*Ability to access resources
*Ability to manage stress
*Being ready for immigration reform

Path Building Method

It is a partnership between the client and our coaches. The Path Building Method has 4 key components (see attachment):
1) We recognize and acknowledge people's strengths
2) Resolve immediate needs (food, homeless prevention, access to resources
3) Identify growth opportunities. Assessment to identify what tools are missing
4) Monitor progress

PROJECT SPECIFICS

Audience = Spanish low-income immigrants "clients".
Message = Help "clients" understand that the acquisition of the "Keys to Rise" is a crucial step towards achieving their personal and family goals.
Product = Tri-Fold Brochure.
Design = Use logo colors; main color blue. Use graphics.

Target Market(s)

Low-income Spanish speaking immigrants

Industry/Entity Type

Community

Font styles to use
Sans Serif

Colors
3276b5
9bcb3c
fece3e
f04a50

Requirements
Must have
• all graphical techniques to communicate the message (drawings, icons, symbols)
Nice to have
• drawings of individuals or families achieving their dreams

```html
<!DOCTYPE html>
<html lang="en">
<head>
<meta charset="utf-8">
<title>Ferndale Union – Keys to Rise</title>
<link rel="stylesheet" href="https://fonts.googleapis.com/css2?family=Open+Sans:wght@400;600;700&family=Roboto+Condensed:wght@300;700&display=swap">
<style>
  :root {
    --brand-blue: #3276b5;
    --brand-navy: #1f5f9e;
    --brand-green: #9bcb3c;
    --brand-yellow: #fece3e;
    --brand-red: #f04a50;
    --cycle-purple: #7b5ea7;
    --cycle-blue: #4a80c2;
    --cycle-red: #c9484b;
    --cycle-green: #8cbf48;
    --paper: #ffffff;
    --ink: #1e1e1e;
  }
  * { margin: 0; padding: 0; box-sizing: border-box; }
  html, body { width: 1200px; height: 849px; overflow: hidden; background: var(--paper); }
  .brochure { position: relative; width: 1200px; height: 849px; overflow: hidden; font-family: "Open Sans", sans-serif; }
  .backdrop { position: absolute; inset: 0; }
  .brand { position: absolute; left: 24px; top: 28px; display: flex; align-items: center; gap: 12px; }
  .brand-mark { width: 54px; height: 54px; background: var(--brand-red); }
  .brand-name { font-family: "Open Sans", sans-serif; font-weight: 600; font-size: 34px; color: var(--brand-navy); letter-spacing: 0.5px; }
  .headline { position: absolute; left: 87px; top: 478px; font-family: "Roboto Condensed", sans-serif; font-weight: 300; font-size: 60px; line-height: 72px; color: var(--brand-red); }
  .skills { position: absolute; left: 443px; top: 448px; list-style: none; color: var(--paper); font-size: 19px; line-height: 34px; }
  .skills li::before { content: ""; display: inline-block; width: 8px; height: 8px; border-radius: 50%; background: var(--paper); margin-right: 9px; vertical-align: middle; position: relative; top: -2px; }
  .website { position: absolute; left: 440px; top: 732px; color: var(--paper); font-size: 31px; }
  .method-title { position: absolute; left: 800px; width: 410px; top: 382px; text-align: center; font-weight: 700; font-size: 21px; color: var(--brand-red); }
  .method-note { position: absolute; left: 939px; top: 545px; width: 130px; text-align: center; font-weight: 700; font-size: 10.5px; line-height: 13px; color: var(--ink); }
  .cycle-label { font-family: "Open Sans", sans-serif; font-weight: 700; font-size: 9.5px; fill: var(--paper); letter-spacing: 0.2px; }
</style>
</head>
<body>
<main class="brochure">
  <svg class="backdrop" width="1200" height="849" viewBox="0 0 1200 849" aria-hidden="false">
    <!-- blue base -->
    <polygon points="0,145 1200,-20 1200,849 0,849" fill="var(--brand-blue)"/>
    <!-- photo band -->
    <g class="photo-band">
      <polygon role="img" aria-label="Photo of a group of adult learners smiling in a classroom" points="0,167 344,120 344,421 0,467" fill="#7e5f55"/>
      <polygon role="img" aria-label="Photo of a teacher helping a student at a computer" points="348,119 657,77 657,379 348,421" fill="#3f8a6c"/>
      <polygon role="img" aria-label="Photo of a student listening attentively in class" points="661,76 867,48 867,351 661,378" fill="#4f5f86"/>
      <polygon role="img" aria-label="Photo of a coach reviewing workbooks with two women" points="871,47 1200,2 1200,306 871,350" fill="#cdbfb2"/>
    </g>
    <!-- left white panel -->
    <polygon points="0,462 400,428 400,795 0,826" fill="var(--paper)"/>
    <!-- right white panel -->
    <polygon points="800,344 1200,313 1200,770 800,790" fill="var(--paper)"/>

    <!-- cycle diagram -->
    <g class="cycle" transform="translate(1004 590)">
      <defs>
        <path id="arc-p1" d="M -141 0 A141 141 0 0 1 0 -141"/>
        <path id="arc-p2" d="M -127 0 A127 127 0 0 1 0 -127"/>
        <path id="arc-b1" d="M 0 -143 A143 143 0 0 1 143 0"/>
        <path id="arc-b2" d="M 0 -129 A129 129 0 0 1 129 0"/>
        <path id="arc-b3" d="M 0 -115 A115 115 0 0 1 115 0"/>
        <path id="arc-r1" d="M 0 104 A104 104 0 0 0 104 0"/>
        <path id="arc-r2" d="M 0 118 A118 118 0 0 0 118 0"/>
        <path id="arc-r3" d="M 0 132 A132 132 0 0 0 132 0"/>
        <path id="arc-g1" d="M -120 0 A120 120 0 0 0 0 120"/>
      </defs>
      <path d="M -164 0 A164 164 0 0 1 0 -164 L 0 -80 A80 80 0 0 0 -80 0 Z" fill="var(--cycle-purple)"/>
      <path d="M 0 -164 A164 164 0 0 1 164 0 L 80 0 A80 80 0 0 0 0 -80 Z" fill="var(--cycle-blue)"/>
      <path d="M 164 0 A164 164 0 0 1 0 164 L 0 80 A80 80 0 0 0 80 0 Z" fill="var(--cycle-red)"/>
      <path d="M 0 164 A164 164 0 0 1 -164 0 L -80 0 A80 80 0 0 0 0 80 Z" fill="var(--cycle-green)"/>
      <circle r="80" fill="var(--paper)"/>
      <!-- flow arrows -->
      <g fill="var(--paper)">
        <polygon points="-8,-98 8,-90 -8,-82"/>
        <polygon points="98,-8 90,8 82,-8"/>
        <polygon points="8,98 -8,90 8,82"/>
        <polygon points="-98,8 -90,-8 -82,8"/>
      </g>
      <text class="cycle-label"><textPath href="#arc-p1" startOffset="50%" text-anchor="middle">WE RECOGNIZE AND ACKNOWLEDGE</textPath></text>
      <text class="cycle-label"><textPath href="#arc-p2" startOffset="50%" text-anchor="middle">PEOPLE'S STRENGTHS</textPath></text>
      <text class="cycle-label"><textPath href="#arc-b1" startOffset="50%" text-anchor="middle">RESOLVE IMMEDIATE NEEDS (FOOD,</textPath></text>
      <text class="cycle-label"><textPath href="#arc-b2" startOffset="50%" text-anchor="middle">HOMELESS PREVENTION,</textPath></text>
      <text class="cycle-label"><textPath href="#arc-b3" startOffset="50%" text-anchor="middle">ACCESS TO RESOURCES)</textPath></text>
      <text class="cycle-label"><textPath href="#arc-r3" startOffset="50%" text-anchor="middle">IDENTIFY GROWTH OPPORTUNITIES.</textPath></text>
      <text class="cycle-label"><textPath href="#arc-r2" startOffset="50%" text-anchor="middle">ASSESSMENT TO IDENTIFY</textPath></text>
      <text class="cycle-label"><textPath href="#arc-r1" startOffset="50%" text-anchor="middle">WHAT TOOLS ARE MISSING</textPath></text>
      <text class="cycle-label"><textPath href="#arc-g1" startOffset="50%" text-anchor="middle">MONITOR PROGRESS</textPath></text>
    </g>
  </svg>

  <header class="brand">
    <span class="brand-mark"></span>
    <span class="brand-name">ferndale union</span>
  </header>

  <h1 class="headline">“Keys to<br>Rise” =<br>Skills and<br>Abilities</h1>

  <ul class="skills">
    <li>Bilingual skills (English &amp; Spanish)</li>
    <li>Technology skills</li>
    <li>Work readiness skills</li>
    <li>Financial literacy skills</li>
    <li>Ability to access resources</li>
    <li>Ability to manage stress</li>
    <li>Being ready for immigration reform</li>
  </ul>

  <p class="website">www.ferndaleunion.org</p>

  <h2 class="method-title">Path Building Method</h2>
  <p class="method-note">It is a partnership between the client and our coaches. The Path Building Method has 4 key components.</p>
</main>
</body>
</html>
```